Hi,
We are an accounting firm looking to upgrade the following:
Logo, letterhead, withcomp slips and maybe our business cards. I have attached our original letterhead (sample A) and a letterhead (SAmple B) which we like the design and layout, however I want to stick with the colours of our orginal letterhead (Sample A) but improve and modernise the look with other letter head (Sample B) I have attached both. On the footer of Sample A, we would like to remove the names of the directors but leave EST. 1985 we also want to add the QRT logo ABN and TAX AGENT logo as stated in Sample B , we would like to do a layout for the header similar to SAmple B however maybe a bit more structured.

```html
<!DOCTYPE html>
<html lang="en">
<head>
<meta charset="utf-8">
<title>Brentholm Accountants Letterhead</title>
<link href="https://fonts.googleapis.com/css2?family=Montserrat:wght@400;500;700&display=swap" rel="stylesheet">
<style>
  :root {
    --brand-blue: #1a4fd8;
    --accent-blue: #2b86f7;
    --deep-blue: #2470d8;
    --ink: #111111;
    --paper: #ffffff;
    --badge-grey: #dfe6ee;
    --badge-ring: #c9d3de;
  }
  html, body {
    margin: 0;
    padding: 0;
    overflow: hidden;
    background: var(--paper);
  }
  .letterhead {
    position: relative;
    width: 957px;
    height: 1200px;
    overflow: hidden;
    background: var(--paper);
    font-family: "Montserrat", sans-serif;
    color: var(--ink);
  }
  .decor { position: absolute; }
  .brand {
    position: absolute;
    left: 69px;
    top: 40px;
  }
  .brand-name {
    display: block;
    font-size: 44px;
    font-weight: 700;
    color: var(--brand-blue);
    letter-spacing: -1px;
    line-height: 1;
  }
  .brand-tag {
    display: flex;
    align-items: center;
    gap: 8px;
    margin-top: 6px;
    margin-left: 12px;
    font-size: 22px;
    font-weight: 500;
    line-height: 1;
  }
  .brand-square {
    width: 14px;
    height: 14px;
    background: var(--accent-blue);
  }
  .contact {
    position: absolute;
    right: 30px;
    top: 47px;
    text-align: right;
    font-size: 18px;
    font-weight: 400;
    line-height: 29.5px;
  }
  .contact-row {
    display: flex;
    justify-content: flex-end;
    align-items: center;
    gap: 6px;
    white-space: nowrap;
  }
  .contact-item {
    display: inline-flex;
    align-items: center;
    gap: 6px;
    margin-left: 8px;
  }
  .icon { width: 22px; height: 22px; fill: var(--brand-blue); }
  .firm-details {
    position: absolute;
    left: 69px;
    top: 1071px;
    font-size: 19.5px;
    line-height: 28px;
  }
  .firm-details p { margin: 0; }
  .firm-details .designation { margin-top: 18px; }
  .badge { position: absolute; }
</style>
</head>
<body>
<div class="letterhead">

  <svg class="decor" style="left:0;top:0" width="260" height="140" viewBox="0 0 260 140" aria-hidden="true">
    <g fill="var(--accent-blue)">
      <polygon points="115,21 149,0 163,0 129,21"/>
      <polygon points="146,21 180,0 204,0 170,21"/>
      <polygon points="197,21 231,0 236,0 224,0 198,21"/>
      <polygon points="176,21 210,0 235,0 201,21"/>
      <polygon points="2,87 46,63 46,75 2,100"/>
      <polygon points="2,106 46,81 46,94 2,118"/>
      <polygon points="2,124 46,99 46,112 2,136"/>
    </g>
  </svg>

  <svg class="decor" style="left:0;top:290px" width="30" height="720" viewBox="0 0 30 720" aria-hidden="true">
    <polygon points="0,0 21,26 21,694 0,720" fill="var(--accent-blue)"/>
    <rect x="21" y="132" width="9" height="489" fill="var(--deep-blue)"/>
  </svg>
  <svg class="decor" style="left:927px;top:290px" width="30" height="720" viewBox="0 0 30 720" aria-hidden="true">
    <polygon points="30,0 9,26 9,694 30,720" fill="var(--accent-blue)"/>
    <rect x="0" y="132" width="9" height="489" fill="var(--deep-blue)"/>
  </svg>

  <header class="brand">
    <span class="brand-name">Brentholm</span>
    <span class="brand-tag"><span class="brand-square"></span>Accountants</span>
  </header>

  <address class="contact" style="font-style:normal">
    <div class="contact-row">
      <span class="contact-item">
        <svg class="icon" viewBox="0 0 24 24" aria-hidden="true"><path d="M6.6 10.8a15.2 15.2 0 0 0 6.6 6.6l2.2-2.2c.3-.3.7-.4 1-.2 1.1.4 2.3.6 3.6.6.6 0 1 .4 1 1V20c0 .6-.4 1-1 1A17 17 0 0 1 3 4c0-.6.4-1 1-1h3.5c.6 0 1 .4 1 1 0 1.3.2 2.5.6 3.6.1.3 0 .7-.2 1z"/></svg>
        +61 3 9000 1234
      </span>
      <span class="contact-item">
        <svg class="icon" viewBox="0 0 24 24" aria-hidden="true"><path d="M7 3h10v4H7zM4 8h16a2 2 0 0 1 2 2v6h-4v5H6v-5H2v-6a2 2 0 0 1 2-2zm4 8v3h8v-3z"/></svg>
        +61 3 9000 5678
      </span>
      <span class="contact-item">
        <svg class="icon" viewBox="0 0 24 24" aria-hidden="true"><path d="M2 5h20v14H2zm2 2v.5l8 5.5 8-5.5V7z"/></svg>
        info@brentholm.com.au
      </span>
    </div>
    <div class="contact-row">
      <svg class="icon" viewBox="0 0 24 24" aria-hidden="true"><path d="M12 2a7 7 0 0 0-7 7c0 5 7 13 7 13s7-8 7-13a7 7 0 0 0-7-7zm0 9.5A2.5 2.5 0 1 1 12 6.5a2.5 2.5 0 0 1 0 5z"/></svg>
      Brentholm Pty Ltd,&nbsp; 48 Elm Grove,&nbsp; Ashwood VIC 3147
    </div>
    <div class="contact-row">
      <svg class="icon" viewBox="0 0 24 24" aria-hidden="true"><path d="M12 2a10 10 0 1 0 0 20 10 10 0 0 0 0-20zm6.9 6h-3a15 15 0 0 0-1.4-3.9A8 8 0 0 1 18.9 8zM12 4a13 13 0 0 1 1.9 4h-3.8A13 13 0 0 1 12 4zM4.3 14a8 8 0 0 1 0-4h3.4a16 16 0 0 0 0 4zm.8 2h3a15 15 0 0 0 1.4 3.9A8 8 0 0 1 5.1 16zm3-8h-3a8 8 0 0 1 4.4-3.9A15 15 0 0 0 8.1 8zM12 20a13 13 0 0 1-1.9-4h3.8A13 13 0 0 1 12 20zm2.3-6H9.7a14 14 0 0 1 0-4h4.6a14 14 0 0 1 0 4zm.2 5.9a15 15 0 0 0 1.4-3.9h3a8 8 0 0 1-4.4 3.9zm1.8-5.9a16 16 0 0 0 0-4h3.4a8 8 0 0 1 0 4z"/></svg>
      www.brentholmaccountants.com.au
    </div>
  </address>

  <footer class="firm-details">
    <p>Established. 1985</p>
    <p>Brentholm Accountants Pty, Limited</p>
    <p>ABN 12 345 678 901</p>
    <p class="designation">Qualified Registered Tax Accountants</p>
  </footer>

  <svg class="badge" style="left:440px;top:1009px" width="270" height="160" viewBox="0 0 270 160" aria-hidden="true">
    <rect x="0" y="0" width="270" height="160" rx="10" fill="var(--badge-grey)"/>
  </svg>

  <svg class="badge" style="left:744px;top:1011px" width="126" height="126" viewBox="0 0 126 126" aria-hidden="true">
    <circle cx="63" cy="63" r="61" fill="var(--badge-grey)" stroke="var(--badge-ring)" stroke-width="2"/>
  </svg>

</div>
</body>
</html>
```